International Wine events organiser seeks simple but stunning business card

I am a freelance events, marketing and PR provider specialised in the Wine industry. I help wineries and wine regions reach trade and consumers in foreign markets through events, help with the websites and communications, press trips and promotional activities. I am looking for a business card which is simple yet effective and is linked to events and communication.

I work mainly - but exclusively - with Italian wineries organising events for them in foreign market.s

I would like to use red in the logo as my present website (lunabrendor.com) used grey and red (although I will be changing the design at a later date).

Target Market(s)

Wine producers, promotional bodies in wine sector, companies looking to hire event organisers,

Industry/Entity Type

Marketing

Requirements
Must have
• My Name - Luna Brendor
My address
My phone
My website : www.lunabrendor.com
my Blog : pebbleandtwig.me

Should not have
• Butterflies, stars, flowers, anything not particularly linked to wine - would like to keep it simple, modern and eye-catching without being too cliche.

```html
<!DOCTYPE html>
<html lang="en">
<head>
<meta charset="utf-8">
<title>Luna Brendor – Business Card</title>
<link rel="stylesheet" href="https://fonts.googleapis.com/css2?family=Open+Sans:wght@300;400;600&display=swap">
<style>
  :root {
    --page: #e9e6e2;
    --card: #ffffff;
    --ink: #4a4a4a;
    --wine: #d8374c;
    --wine-deep: #b42436;
    --wine-soft: #e4687a;
    --photo-light: #f3e9ea;
    --photo-mid: #c9545f;
    --photo-dark: #7d1a24;
  }
  * { box-sizing: border-box; margin: 0; padding: 0; }
  html, body {
    width: 1200px; height: 900px; overflow: hidden;
    background: var(--page);
    font-family: "Open Sans", sans-serif;
  }
  .canvas {
    position: relative; width: 1200px; height: 900px;
    display: flex; flex-direction: column; align-items: center; justify-content: center; gap: 50px;
  }
  .card {
    position: relative; width: 630px; height: 360px;
    background: var(--card);
    box-shadow: 0 8px 24px rgba(0,0,0,.18);
    overflow: hidden;
  }

  /* Front */
  .front__brand {
    position: absolute; left: 34px; top: 30px;
    font-size: 50px; font-weight: 400; letter-spacing: 1px;
    color: var(--wine); line-height: 1;
  }
  .front__tagline {
    position: absolute; left: 36px; top: 88px;
    font-size: 13.5px; letter-spacing: .6px; text-transform: uppercase;
    color: var(--ink);
  }
  .front__tagline em { font-style: normal; color: var(--wine); }
  .front__photo {
    position: absolute; left: 0; top: 120px; width: 100%; height: 240px;
    background:
      radial-gradient(ellipse 40% 45% at 32% 50%, var(--photo-dark), var(--photo-mid) 55%, transparent 80%),
      linear-gradient(180deg, var(--card), var(--photo-light));
  }

  /* Back */
  .back { display: flex; }
  .back__edge { width: 16px; background: var(--wine); }
  .back__art-area {
    flex: 0 0 44%; display: flex; align-items: center; justify-content: center;
  }
  .back__illustration {
    width: 190px; height: 230px; border-radius: 40% 40% 30% 30%;
    background: radial-gradient(ellipse at center, var(--wine-soft), rgba(216,55,76,.15) 70%, transparent);
  }
  .back__panel {
    flex: 1; color: #fff; padding: 44px 34px 0 34px;
    background: linear-gradient(160deg, var(--wine-soft), var(--wine) 55%, var(--wine-deep));
  }
  .contact__name { font-size: 27px; font-weight: 300; line-height: 1.1; }
  .contact__role { font-size: 13.5px; font-weight: 300; line-height: 1.35; margin: 6px 0 18px; opacity: .95; }
  .contact__list { list-style: none; font-size: 13.5px; font-weight: 400; }
  .contact__item { display: flex; align-items: flex-start; gap: 10px; margin-bottom: 7px; line-height: 1.35; }
  .contact__icon { flex: 0 0 16px; width: 16px; height: 16px; margin-top: 2px; }
  .contact__gap { margin-top: 10px; }
</style>
</head>
<body>
<main class="canvas">

  <section class="card front" aria-label="Card front">
    <h1 class="front__brand">LUNABRENDOR</h1>
    <p class="front__tagline">Communication <em>and events for the world of wine</em></p>
    <div class="front__photo" role="img" aria-label="Photograph of a tipped wine glass spilling red wine"></div>
  </section>

  <section class="card back" aria-label="Card back">
    <div class="back__edge"></div>
    <div class="back__art-area">
      <div class="back__illustration" role="img" aria-label="Red line illustration of a woman in a hat and long dress raising a wine glass"></div>
    </div>
    <div class="back__panel">
      <h2 class="contact__name">Luna Brendor</h2>
      <p class="contact__role">Specialist in communication,<br>events and PR for the wine industry</p>
      <ul class="contact__list">
        <li class="contact__item">
          <svg class="contact__icon" viewBox="0 0 16 16" aria-hidden="true"><path fill="#fff" d="M3.5 1.5l2.5 3-1.4 1.6a9 9 0 0 0 5.3 5.3l1.6-1.4 3 2.5-1.5 2A12 12 0 0 1 1.5 3z"/></svg>
          <span>+49 170 5512 384</span>
        </li>
        <li class="contact__item">
          <svg class="contact__icon" viewBox="0 0 16 16" aria-hidden="true"><path fill="#fff" d="M8 1a5 5 0 0 0-5 5c0 3.8 5 9 5 9s5-5.2 5-9a5 5 0 0 0-5-5zm0 7a2 2 0 1 1 0-4 2 2 0 0 1 0 4z"/></svg>
          <span>Lindenhofer Strasse, 12<br>80331 Altheim</span>
        </li>
        <li class="contact__item contact__gap">
          <svg class="contact__icon" viewBox="0 0 16 16" aria-hidden="true"><circle cx="8" cy="8" r="8" fill="#fff"/><text x="8" y="11.5" text-anchor="middle" font-size="10" font-family="Open Sans, sans-serif" fill="#d8374c">@</text></svg>
          <span>luna@lunabrendor.com</span>
        </li>
        <li class="contact__item">
          <svg class="contact__icon" viewBox="0 0 16 16" aria-hidden="true"><circle cx="8" cy="8" r="8" fill="#fff"/><circle cx="8" cy="8" r="4.5" fill="none" stroke="#d8374c" stroke-width="1.2"/><path d="M3.5 8h9M8 3.5v9" stroke="#d8374c" stroke-width="1"/></svg>
          <span>www.lunabrendor.com</span>
        </li>
        <li class="contact__item">
          <svg class="contact__icon" viewBox="0 0 16 16" aria-hidden="true"><circle cx="8" cy="8" r="8" fill="#fff"/></svg>
          <span>chirpline.net/Pebbleandtwig78</span>
        </li>
      </ul>
    </div>
  </section>

</main>
</body>
</html>
```